Criação de Papelaria Profissional para Limpeza & Serviço para o lar
" Nossa empresa e familiar, buscamos fazer nosso trabalho com excelencia e qualidade visando o bem estar de nossos clientes. "

```html
<!DOCTYPE html>
<html lang="en">
<head>
<meta charset="utf-8">
<title>HearthNest Folder</title>
<link href="https://fonts.googleapis.com/css2?family=Poppins:wght@400;700&display=swap" rel="stylesheet">
<style>
  :root {
    --backdrop: #d3ddd8;
    --brand-green: #3aa886;
    --brand-green-deep: #2f8f72;
    --paper: #f7f8f7;
    --copper: #c98b55;
    --fold-shadow: rgba(0, 0, 0, 0.08);
  }
  html, body {
    margin: 0;
    padding: 0;
    width: 1200px;
    height: 1200px;
    overflow: hidden;
    background: var(--backdrop);
    font-family: "Poppins", sans-serif;
  }
  .canvas {
    position: relative;
    width: 1200px;
    height: 1200px;
    display: flex;
    align-items: center;
    justify-content: center;
  }
  .folder-spread {
    position: relative;
    width: 1040px;
    height: 740px;
    display: flex;
    box-shadow: 0 20px 40px rgba(0, 0, 0, 0.12);
  }
  .panel {
    position: relative;
    width: 520px;
    height: 740px;
    overflow: hidden;
  }
  .panel--back {
    background: linear-gradient(90deg, var(--brand-green-deep) 0%, var(--brand-green) 45%, #9fd3c1 78%, var(--paper) 100%);
  }
  .panel--front {
    background: var(--paper);
    box-shadow: inset 12px 0 18px -10px var(--fold-shadow);
  }
  .back-brand {
    position: absolute;
    left: 60px;
    top: 70px;
    transform-origin: left top;
    transform: rotate(90deg) translateY(-100%);
    font-weight: 700;
    font-size: 54px;
    line-height: 1;
    color: var(--brand-green-deep);
    filter: brightness(0.8);
    white-space: nowrap;
  }
  .back-contact {
    position: absolute;
    left: 40px;
    bottom: 120px;
    transform-origin: left bottom;
    transform: rotate(90deg) translateX(-100%);
    font-size: 11px;
    line-height: 1.7;
    color: #e6f3ee;
    white-space: nowrap;
  }
  .back-contact p { margin: 0; }
  .front-logo {
    position: absolute;
    right: 40px;
    top: 260px;
    transform-origin: right top;
    transform: rotate(90deg) translateX(100%);
    display: flex;
    align-items: center;
    gap: 14px;
    white-space: nowrap;
  }
  .front-logo__dot {
    width: 44px;
    height: 44px;
    border-radius: 50%;
    background: var(--copper);
  }
  .front-logo__name {
    font-weight: 700;
    font-size: 52px;
    line-height: 1;
    color: var(--brand-green);
  }
</style>
</head>
<body>
  <main class="canvas">
    <section class="folder-spread">
      <div class="panel panel--back">
        <div class="back-brand">HearthNest</div>
        <div class="back-contact">
          <p>(555) 014-2288</p>
          <p>hearthnestcleaning</p>
          <p>hello@hearthnest.com</p>
        </div>
      </div>
      <div class="panel panel--front">
        <div class="front-logo">
          <span class="front-logo__dot"></span>
          <span class="front-logo__name">HearthNest</span>
        </div>
      </div>
    </section>
  </main>
</body>
</html>
```